Landing Page Design

We need a landing page template designed to support a clients Zintro Bidlink Campaigns. The client is called Merrow Plumbing and they install and repair hot water systems (only). They provide no other plumbing services.

We are really looking for a great looking landing page that is both engaging and functional.

Target Market(s)

Residential/Domestic market. Typically wives and partners who are typically home or run the household.

Industry/Entity Type

Plumbing

Number of Pages Required

1 page

Requirements
Must have
• Strong branding
Strong call to actions
Great and obvious looking buttons
Nice to have
• Smart use of colour
Should not have
• The design should not use old-style, serif fonts.

Do not include any plumbing images

```html
<!DOCTYPE html>
<html lang="en">
<head>
<meta charset="utf-8">
<title>Merrow Plumbing – Solar Hot Water Systems</title>
<link rel="stylesheet" href="https://fonts.googleapis.com/css2?family=Ubuntu:ital,wght@0,400;0,500;0,700;1,400;1,700&display=swap">
<style>
:root{
  --sea-deep:#0a86a8;
  --sea-mid:#1fb0cf;
  --sea-light:#5fd0e6;
  --panel-top:#c9f0f8;
  --panel-bottom:#7fd4e6;
  --white:#ffffff;
  --ink:#3a3a3a;
  --navy:#14506e;
  --heading:#1c6e9c;
  --brand-red:#e0262b;
  --orange-top:#ffd23a;
  --orange-bottom:#f7a212;
  --blue-btn-top:#2f86cf;
  --blue-btn-bottom:#135ea6;
  --green-btn-top:#72c523;
  --green-btn-bottom:#3f9a12;
  --slate-top:#6b8791;
  --slate-bottom:#4a6670;
  --form-bg:#f2f2f2;
  --field-border:#a9a9a9;
}
*{box-sizing:border-box;margin:0;padding:0}
html,body{width:1200px;height:963px;overflow:hidden}
body{
  position:relative;
  font-family:"Ubuntu",Arial,sans-serif;
  color:var(--ink);
  background:
    radial-gradient(ellipse 520px 420px at 80px 0,rgba(255,255,255,.75),rgba(255,255,255,0) 70%),
    linear-gradient(180deg,var(--sea-light) 0%,var(--sea-mid) 45%,var(--sea-deep) 100%);
}
.frame{position:absolute;left:0;top:0}
.call-now{position:absolute;left:722px;top:40px;color:var(--white);font-size:28px;font-weight:500;letter-spacing:.5px;text-shadow:0 1px 2px rgba(0,0,0,.25)}
.call-now strong{font-size:35px;font-weight:700;letter-spacing:1px}

.brand{position:absolute;left:114px;top:118px;display:flex;align-items:center;gap:10px}
.brand-dot{width:26px;height:26px;border-radius:50%;background:var(--brand-red)}
.brand-name{font-size:34px;font-weight:700;color:var(--brand-red);letter-spacing:.5px;line-height:1}

.tagline{position:absolute;left:396px;top:188px;color:var(--navy);font-size:27px;font-weight:700;font-style:italic}
.tagline span{font-style:normal;font-size:22px;margin-left:10px;letter-spacing:1px}

.benefits{position:absolute;left:885px;top:107px;list-style:none;color:var(--navy);font-size:16px;font-weight:500;line-height:23.4px}
.benefits li::before{content:"• "}

.content{position:absolute;left:91px;top:234px;width:1052px;height:680px;background:var(--white);border-radius:10px}

.section-title{position:absolute;left:120px;top:258px;color:var(--heading);font-size:22px;font-weight:700;letter-spacing:.3px}
.intro{position:absolute;left:121px;top:309px;width:450px;font-size:15px;line-height:23.4px;color:var(--ink)}
.intro p{margin-bottom:23.4px}

.hero-photo{position:absolute;left:584px;top:284px;width:240px;height:372px;transform:rotate(3deg);background:var(--white);padding:8px;box-shadow:0 3px 10px rgba(0,0,0,.35)}
.hero-photo div{width:100%;height:100%;background:linear-gradient(160deg,#d7d9da 0%,#9ea3a6 45%,#5e6366 100%)}

.btn{position:absolute;display:flex;align-items:center;justify-content:center;text-align:center;color:var(--white);font-weight:700;font-size:23px;line-height:26px;text-transform:uppercase;border-radius:3px;text-shadow:0 1px 2px rgba(0,0,0,.4);box-shadow:0 2px 4px rgba(0,0,0,.3)}
.btn-quote{left:137px;top:603px;width:164px;height:88px;background:linear-gradient(180deg,var(--blue-btn-top),var(--blue-btn-bottom));border:2px solid #0e4f8c}
.btn-site{left:367px;top:603px;width:164px;height:88px;background:linear-gradient(180deg,var(--green-btn-top),var(--green-btn-bottom));border:2px solid #358410}

.rebate-banner{position:absolute;left:76px;top:762px;width:566px;height:76px;display:flex;align-items:center;padding-left:38px;color:var(--white);font-size:23px;font-weight:500;letter-spacing:.8px;background:linear-gradient(180deg,var(--slate-top),var(--slate-bottom));border-radius:0 10px 10px 0;box-shadow:0 3px 6px rgba(0,0,0,.3)}
.rebate-fold{position:absolute;left:76px;top:838px}

.enquiry{position:absolute;left:818px;top:253px;width:275px;height:641px;background:var(--form-bg);border:1px solid #d4d4d4;border-radius:6px;overflow:hidden}
.enquiry-head{height:145px;background:linear-gradient(180deg,var(--orange-top),var(--orange-bottom));text-align:center;color:#222;padding-top:14px}
.enquiry-head em{display:block;font-size:15px}
.enquiry-head .line{font-size:17px;line-height:24px}
.enquiry-head .phone{font-size:27px;font-weight:700;line-height:32px}
.field{position:absolute;left:17px}
.field label{display:block;font-size:15.5px;color:var(--ink);margin-bottom:4px}
.field input,.field textarea{display:block;width:222px;height:21px;border:1px solid var(--field-border);background:var(--white);font:inherit}
.field textarea{height:99px;resize:none}
.btn-enquire{position:absolute;left:81px;top:577px;width:177px;height:47px;background:linear-gradient(180deg,var(--orange-top),var(--orange-bottom));border:2px solid #e08a00;color:var(--white);font-family:inherit;font-size:21px;font-weight:700;text-transform:uppercase;text-shadow:0 1px 2px rgba(0,0,0,.35);border-radius:2px}
</style>
</head>
<body>

<svg class="frame" width="1200" height="963" viewBox="0 0 1200 963" aria-hidden="true">
  <defs>
    <linearGradient id="panelFill" x1="0" y1="0" x2="0" y2="1">
      <stop offset="0" stop-color="#d2f3fa"/>
      <stop offset="1" stop-color="#78cfe2"/>
    </linearGradient>
  </defs>
  <path d="M85 40 H320 Q334 40 344 56 L352 80 Q360 96 378 96 H1116 Q1127 96 1127 107 V920 Q1127 932 1115 932 H85 Q73 932 73 920 V52 Q73 40 85 40 Z" fill="url(#panelFill)" opacity=".9"/>
</svg>

<p class="call-now">Call NOW on <strong>9471 3058</strong></p>

<div class="brand">
  <span class="brand-dot"></span>
  <span class="brand-name">Merrow Plumbing</span>
</div>

<p class="tagline">Hot Water Now!<span>SAVE $$$</span></p>

<ul class="benefits">
  <li>Sydney 24 Hours 7 Days</li>
  <li>On Time</li>
  <li>Professional Technicians</li>
  <li>We Advise on Rebates</li>
  <li>Authorised Torvane Dealer</li>
</ul>

<main class="content"></main>

<h1 class="section-title">SOLAR HOT WATER SYSTEMS</h1>
<div class="intro">
  <p>Engage our routine office cleaning for at least 6 months and receive a FREE Carpet and Window clean! No strings attached, no contracts.</p>
  <p>To take advantage of this great offer call us on 1300 58 71 40 or complete and submit the form on this page.</p>
  <p>At Brellix we provide all your property service needs - painlessly. We understand that cleaning and other property services should be background activities. A set and forget proposition.</p>
</div>

<figure class="hero-photo"><div role="img" aria-label="Photo of a woman enjoying a warm shower"></div></figure>

<a class="btn btn-quote">Book a<br>free quote</a>
<a class="btn btn-site">Visit our<br>web site</a>

<svg class="rebate-fold" width="16" height="14" viewBox="0 0 16 14" aria-hidden="true"><path d="M0 0 H16 L16 14 Z" fill="#2f464e"/></svg>
<a class="rebate-banner">CLICK HERE FOR INFORMATION ON REBATES</a>

<form class="enquiry">
  <div class="enquiry-head">
    <em>Take advantage of this great offer.</em>
    <div class="line">Contact Us <em style="display:inline;font-size:17px">NOW</em> on</div>
    <div class="phone">9471 3058</div>
    <div class="line">or</div>
    <div class="line">register your interest below</div>
  </div>
  <div class="field" style="top:159px"><label>Your First Name:</label><input type="text"></div>
  <div class="field" style="top:213px"><label>Your Surname:</label><input type="text"></div>
  <div class="field" style="top:268px"><label>Your Suburb:</label><input type="text"></div>
  <div class="field" style="top:324px"><label>Best Contact Number:</label><input type="text"></div>
  <div class="field" style="top:380px"><label>Your Email Address:</label><input type="text"></div>
  <div class="field" style="top:436px"><label>Enquiry / Comments:</label><textarea></textarea></div>
  <button class="btn-enquire" type="button">Enquire now</button>
</form>

</body>
</html>
```